Electrician Company Website Design

I am looking to get a website designed only. I do not need it converted ot html. I simply need the design in a psd format. I have my own team for the conversion. The website is for an electrician company called Bramblecourt electric. I have created a txt document with the project parameters and specifics. I have also uploaded their logo in all avaible formats. It's a zip file.

Number of Pages Required

1 page

```html
<!DOCTYPE html>
<html lang="en">
<head>
<meta charset="utf-8">
<title>Bramblecourt Electric</title>
<link href="https://fonts.googleapis.com/css2?family=Oswald:wght@300;400;500&family=Montserrat:wght@400;500;600;700&display=swap" rel="stylesheet">
<style>
:root{
  --red:#b81d25;
  --blue:#1262b8;
  --grey:#7b7b7d;
  --grey-line:#9a9a9c;
  --ink:#222226;
  --white:#ffffff;
}
*{box-sizing:border-box;margin:0;padding:0}
html,body{width:1200px;height:3300px;overflow:hidden;background:var(--white)}
body{position:relative;font-family:"Montserrat",sans-serif;color:var(--ink)}
.abs{position:absolute}
.heading{font-family:"Oswald",sans-serif;font-weight:300;text-transform:uppercase;letter-spacing:.5px}
.heading strong{font-weight:500}
.btn{position:absolute;display:flex;align-items:center;justify-content:center;border-radius:20px;font-weight:700;font-size:10px;text-transform:uppercase;letter-spacing:.5px}

.brand{left:200px;top:36px;display:flex;align-items:center;gap:10px}
.brand-dot{width:26px;height:26px;border-radius:50%;background:var(--red);flex:none}
.brand-name{font-family:"Oswald",sans-serif;font-weight:500;font-size:20px;text-transform:uppercase;line-height:1.1}
.callus{left:590px;top:32px;font-size:12px;font-weight:600;display:flex;align-items:center;gap:6px}
.callus .label{color:var(--red)}
.social{position:absolute;top:25px;width:28px;height:28px;border-radius:50%;background:var(--grey)}
.quote-btn{left:873px;top:24px;width:128px;height:30px;border:2px solid var(--red);color:var(--red)}
.nav{left:473px;top:72px;display:flex;gap:30px;font-size:11px;font-weight:600;text-transform:uppercase}
.nav .active{color:var(--red);border-bottom:1px solid var(--red)}

.hero{left:0;top:102px;width:1200px;height:543px;background:linear-gradient(100deg,#cfd0cf 0%,#b9b8b2 30%,#6f6a55 50%,#c9a24b 65%,#a7a9a4 82%,#d8d9d6 100%)}
.hero-kicker{left:200px;top:214px;color:var(--white);font-size:15px}
.hero-title{left:200px;top:246px;color:var(--white);font-size:38px;font-weight:500}
.hero-btn{left:200px;top:316px;width:112px;height:28px;background:var(--blue);color:var(--white)}
.hero-services{left:0;width:1200px;top:412px;text-align:center;color:var(--white);font-size:15px;font-weight:400}
.service-card{position:absolute;top:461px;width:250px;height:184px;display:flex;align-items:flex-end;justify-content:center;padding-bottom:22px;text-align:center;color:var(--white);font-weight:600;font-size:13px;text-transform:uppercase;line-height:1.35}

.emblem{left:200px;top:700px;width:385px;height:240px;display:flex;align-items:center;justify-content:center;gap:14px}
.emblem-dot{width:50px;height:50px;border-radius:50%;background:var(--red);flex:none}
.emblem-name{font-family:"Oswald",sans-serif;font-weight:500;font-size:30px;text-transform:uppercase}
.welcome{left:613px;top:690px;width:390px}
.welcome h2{font-size:26px;line-height:1.2}
.welcome h3{font-family:"Oswald",sans-serif;font-weight:500;font-size:26px;color:var(--blue);text-transform:uppercase;line-height:1.2}
.welcome .lead{margin-top:16px;font-size:12.5px;font-weight:600;line-height:1.45}
.welcome .body{margin-top:18px;font-size:9.5px;line-height:1.65;color:#444}
.welcome-btn{left:613px;top:948px;width:112px;height:30px;background:var(--red);color:var(--white)}

.gallery{left:0;top:1084px;width:1200px;height:696px;background:var(--red)}
.section-title{left:0;width:1200px;text-align:center;font-size:24px;color:var(--white)}
.tile{position:absolute;display:flex;align-items:flex-end;padding:0 0 18px 24px;color:var(--white);font-size:13px;font-weight:600}
.outline-btn{left:550px;width:100px;height:30px;border:2px solid var(--white);color:var(--white)}

.faq{left:0;top:1780px;width:1200px;height:532px;background:var(--grey)}
.faq-list{left:295px;top:1900px;width:610px}
.faq-item{display:flex;justify-content:space-between;align-items:center;height:38px;border-bottom:1px solid var(--grey-line);padding:0 12px;color:var(--white);font-size:11.5px}
.plus{width:12px;height:12px;border-radius:50%;background:var(--white);position:relative;flex:none}
.plus::before,.plus::after{content:"";position:absolute;background:var(--grey);left:3px;top:5.5px;width:6px;height:1px}
.plus::after{transform:rotate(90deg)}
.faq-open{background:var(--red);padding:10px 12px 12px;color:var(--white)}
.faq-open .q{display:flex;justify-content:space-between;font-size:12px;font-weight:600}
.faq-open p{margin-top:8px;font-size:8.5px;line-height:1.6}
.faq-open .plus::before{background:var(--red)}
.faq-open .plus::after{display:none}
.faq-btn{left:550px;top:2186px;width:100px;height:30px;border:2px solid var(--red);color:var(--red)}
.faq-mark{left:905px;top:2205px;width:190px;text-align:center;font-family:"Oswald",sans-serif;font-weight:500;font-size:22px;color:#e4e4e6;text-transform:uppercase;line-height:1.15}

.watermark{left:250px;top:2340px;font-family:"Oswald",sans-serif;font-weight:500;font-size:54px;color:#f4f4f5;text-transform:uppercase}
.areas{left:200px;top:2450px;width:470px}
.areas h2{font-size:26px}
.areas h2 strong{color:var(--blue)}
.areas p{margin-top:10px;font-size:11px;line-height:1.5}
.area-list{margin-top:18px;display:grid;grid-template-columns:160px 178px 130px;row-gap:24px;font-family:"Oswald",sans-serif;font-size:11px;text-transform:uppercase}
.area-list span{display:flex;align-items:center;gap:10px}
.areas-btn{left:200px;top:2628px;width:112px;height:30px;border:2px solid var(--red);color:var(--red)}
.form-shadow{left:722px;top:2432px;width:210px;height:230px;background:var(--red)}
.form{left:741px;top:2451px;width:250px;height:297px;background:var(--grey);color:var(--white)}
.form-title{text-align:center;padding-top:18px;font-size:15px;line-height:1.45}
.field{margin:0 18px;height:38px;border-bottom:1px solid var(--grey-line);display:flex;align-items:flex-end;justify-content:space-between;padding:0 0 8px 2px;font-size:9px}
.form-foot{position:absolute;left:18px;right:-10px;bottom:22px;display:flex;justify-content:space-between;align-items:center;font-size:11px}
.form-foot .tel{display:flex;align-items:center;gap:8px}
.submit{position:static;width:100px;height:30px;background:var(--red);color:var(--white)}

.footer{left:0;top:2766px;width:1200px;height:469px;background:linear-gradient(180deg,#3a3a3d,#262628)}
.foot-brand{left:200px;top:2985px;display:flex;align-items:center;gap:10px}
.foot-brand .brand-name{color:var(--white);font-size:17px}
.foot-col{top:2956px;color:var(--white)}
.foot-col h4{font-family:"Oswald",sans-serif;font-weight:400;font-size:13px;text-transform:uppercase;margin-bottom:16px}
.foot-col li{list-style:none;font-size:8.5px;line-height:19px;color:#d8d8d8}
.contact-line{display:flex;gap:10px;align-items:flex-start;font-size:9px;line-height:1.6;margin-bottom:12px;color:#ddd}
.contact-line.big{font-size:14px}
.foot-social{position:absolute;left:969px;width:28px;height:28px;border-radius:50%;background:var(--grey)}
.copyright{left:200px;top:3170px;font-size:8px;color:#999}
.legal{left:612px;top:3170px;font-size:8px;color:#999;display:flex;gap:14px}
</style>
</head>
<body>

<!-- header -->
<div class="abs brand"><span class="brand-dot"></span><span class="brand-name">Bramblecourt Electric</span></div>
<div class="abs callus"><span class="label">Call Us:</span>
  <svg width="12" height="12" viewBox="0 0 24 24"><path d="M6.6 10.8a15 15 0 006.6 6.6l2.2-2.2a1 1 0 011-.25 11.4 11.4 0 003.6.57 1 1 0 011 1V20a1 1 0 01-1 1A17 17 0 013 4a1 1 0 011-1h3.5a1 1 0 011 1c0 1.25.2 2.45.57 3.57a1 1 0 01-.25 1z" fill="#b81d25"/></svg>
  <span>555 014 2290</span></div>
<span class="social" style="left:752px"></span>
<span class="social" style="left:788px;background:var(--red)"></span>
<span class="social" style="left:824px"></span>
<div class="btn quote-btn">Get a free quote</div>
<nav class="abs nav">
  <span class="active">Home</span><span>Company</span><span>Services</span><span>Service Area</span><span>Gallery</span><span>FAQs</span><span>Contact Us</span>
</nav>

<!-- hero -->
<div class="abs hero" role="img" aria-label="Photo of a smiling electrician in a hard hat working on a wiring panel"></div>
<svg class="abs" style="left:0;top:102px" width="1200" height="543" viewBox="0 0 1200 543">
  <path d="M0,470 Q420,330 1200,480 L1200,543 L0,543 Z" fill="#ffffff"/>
  <path d="M0,462 Q420,322 1200,472" fill="none" stroke="#1262b8" stroke-width="7"/>
</svg>
<div class="abs heading hero-kicker">We provide electrical services and</div>
<div class="abs heading hero-title">Highly experienced electricians</div>
<div class="btn hero-btn">Contact us</div>
<div class="abs heading hero-services">Our services</div>
<div class="service-card" style="left:200px;background:linear-gradient(180deg,#c98a86,#b8343a)" role="img" aria-label="Commercial interior photo">Commerical electrical<br>services</div>
<div class="service-card" style="left:475px;background:linear-gradient(180deg,#4f8fc8,#1d5fa8)" role="img" aria-label="Modern house photo">Residential electrical<br>services</div>
<div class="service-card" style="left:750px;background:linear-gradient(180deg,#5a6f8c,#1f2e4a)" role="img" aria-label="Industrial plant photo">Industrial electrical<br>services</div>

<!-- welcome -->
<div class="abs emblem"><span class="emblem-dot"></span><span class="emblem-name">Bramblecourt Electric</span></div>
<div class="abs welcome">
  <h2 class="heading">Welcome to</h2>
  <h3>Bramblecourt Electric.</h3>
  <p class="lead">Lorem Ipsum is simply dummy text of the printing and typesetting industry.</p>
  <p class="body">It is a long established fact that a reader will be distracted by the readable content of a page when looking at its layout. The point of using Lorem Ipsum is that it has a more-or-less normal distribution of letters, as opposed to using 'Content here, content here', making it look like readable English. Many desktop publishing uncover many web sites still in their infancy ...</p>
</div>
<div class="btn welcome-btn">Discover more</div>

<!-- gallery -->
<svg class="abs" style="left:0;top:1000px" width="1200" height="90" viewBox="0 0 1200 90">
  <path d="M40,58 C330,-10 700,100 1180,20" fill="none" stroke="#8a8a8c" stroke-width="9"/>
  <path d="M0,90 L0,70 C320,0 700,110 1200,30 L1200,90 Z" fill="#b81d25"/>
</svg>
<div class="abs gallery"></div>
<div class="abs heading section-title" style="top:1192px">Past <strong>Project Gallery</strong></div>
<div class="tile" style="left:200px;top:1251px;width:250px;height:188px;background:linear-gradient(160deg,#9aa3b0,#5b5248)" role="img" aria-label="Residential living room photo">Residential</div>
<div class="tile" style="left:475px;top:1251px;width:250px;height:188px;background:linear-gradient(160deg,#b7b7b5,#4c4c4d)" role="img" aria-label="Commercial lobby photo">Commerical</div>
<div class="tile" style="left:750px;top:1251px;width:250px;height:188px;background:linear-gradient(160deg,#c0874a,#4a2f1d)" role="img" aria-label="Commercial restaurant photo">Commerical</div>
<div class="tile" style="left:200px;top:1470px;width:388px;height:188px;background:linear-gradient(180deg,#5b7fb8,#c08a5c)" role="img" aria-label="Industrial refinery photo">Industrial</div>
<div class="tile" style="left:612px;top:1470px;width:388px;height:188px;background:linear-gradient(180deg,#3d5a86,#6b5a3a)" role="img" aria-label="Residential house at dusk photo">Residential</div>
<div class="btn outline-btn" style="top:1704px">View all</div>

<!-- faq -->
<div class="abs faq"></div>
<div class="abs heading section-title" style="top:1842px">Frequently <strong>asked question</strong></div>
<div class="abs faq-list">
  <div class="faq-item"><span>There are many variations of passages of Lorem Ipsum?</span><span class="plus"></span></div>
  <div class="faq-open">
    <div class="q"><span>Contrary to popular belief?</span><span class="plus"></span></div>
    <p>But I must explain to you how all this mistaken idea of denouncing pleasure and praising pain was born and I will give you a complete account of the system, and expound the actual teachings of the great explorer of the truth, the master-builder of human happiness. No one rejects, dislikes, or avoids pleasure itself, because it is pleasure.</p>
  </div>
  <div class="faq-item"><span>Sed ut perspiciatis unde omnis iste natus error?</span><span class="plus"></span></div>
  <div class="faq-item"><span>At vero eos et accusamus et iusto odio dignissimos?</span><span class="plus"></span></div>
  <div class="faq-item"><span>On the other hand, we denounce with righteous indignation?</span><span class="plus"></span></div>
</div>
<div class="btn faq-btn">View all</div>
<svg class="abs" style="left:0;top:2218px" width="1200" height="100" viewBox="0 0 1200 100">
  <path d="M0,100 L0,86 C380,0 780,60 1200,52 L1200,100 Z" fill="#ffffff"/>
  <path d="M0,82 C380,-4 780,56 1200,48" fill="none" stroke="#b81d25" stroke-width="8"/>
</svg>
<div class="abs faq-mark">Bramblecourt<br>Electric</div>

<!-- service areas -->
<div class="abs watermark">Bramblecourt</div>
<div class="abs areas">
  <h2 class="heading">Service <strong>Areas</strong></h2>
  <p>Lorem ipsum dolor sit amet, consectetur adipiscing elit, sed do eiusmod tempor incididunt ut labore et dolore magna aliqua.</p>
  <div class="area-list">
    <span><svg width="10" height="13" viewBox="0 0 10 13"><path d="M5 0a5 5 0 015 5c0 3.5-5 8-5 8S0 8.5 0 5a5 5 0 015-5z" fill="#b81d25"/><circle cx="5" cy="5" r="1.8" fill="#fff"/></svg>Central Minnesota</span>
    <span><svg width="10" height="13" viewBox="0 0 10 13"><path d="M5 0a5 5 0 015 5c0 3.5-5 8-5 8S0 8.5 0 5a5 5 0 015-5z" fill="#b81d25"/><circle cx="5" cy="5" r="1.8" fill="#fff"/></svg>Contrary to popular</span>
    <span><svg width="10" height="13" viewBox="0 0 10 13"><path d="M5 0a5 5 0 015 5c0 3.5-5 8-5 8S0 8.5 0 5a5 5 0 015-5z" fill="#b81d25"/><circle cx="5" cy="5" r="1.8" fill="#fff"/></svg>Simply dummy tex</span>
    <span><svg width="10" height="13" viewBox="0 0 10 13"><path d="M5 0a5 5 0 015 5c0 3.5-5 8-5 8S0 8.5 0 5a5 5 0 015-5z" fill="#b81d25"/><circle cx="5" cy="5" r="1.8" fill="#fff"/></svg>Simply dummy tex</span>
    <span><svg width="10" height="13" viewBox="0 0 10 13"><path d="M5 0a5 5 0 015 5c0 3.5-5 8-5 8S0 8.5 0 5a5 5 0 015-5z" fill="#b81d25"/><circle cx="5" cy="5" r="1.8" fill="#fff"/></svg>Sed ut perspiciatis</span>
  </div>
</div>
<div class="btn areas-btn">Discover more</div>
<div class="abs form-shadow"></div>
<div class="abs form">
  <div class="heading form-title">Bramblecourt Electric<br><strong>Get a free quote</strong></div>
  <div class="field"><span>Name</span></div>
  <div class="field"><span>Email</span></div>
  <div class="field"><span>Phone</span></div>
  <div class="field"><span>Services</span><span>&#8964;</span></div>
  <div class="form-foot">
    <span class="tel"><svg width="14" height="14" viewBox="0 0 24 24"><path d="M6.6 10.8a15 15 0 006.6 6.6l2.2-2.2a1 1 0 011-.25 11.4 11.4 0 003.6.57 1 1 0 011 1V20a1 1 0 01-1 1A17 17 0 013 4a1 1 0 011-1h3.5a1 1 0 011 1c0 1.25.2 2.45.57 3.57a1 1 0 01-.25 1z" fill="none" stroke="#b81d25" stroke-width="2"/></svg>555 014 2290</span>
    <span class="btn submit">Submit</span>
  </div>
</div>

<!-- footer -->
<div class="abs footer" role="img" aria-label="Dimmed photo of a furnished interior behind the footer"></div>
<svg class="abs" style="left:0;top:2740px" width="1200" height="110" viewBox="0 0 1200 110">
  <path d="M0,110 L0,50 C380,-10 780,80 1200,30 L1200,110 Z" fill="#8a8a8c"/>
  <path d="M0,110 L0,62 C380,4 780,92 1200,44 L1200,110 Z" fill="#3a3a3d"/>
</svg>
<div class="abs foot-brand"><span class="brand-dot"></span><span class="brand-name">Bramblecourt<br>Electric</span></div>
<div class="abs foot-col" style="left:406px">
  <h4>Contact us</h4>
  <div class="contact-line big">555 014 2290</div>
  <div class="contact-line"><svg width="11" height="9" viewBox="0 0 11 9"><rect width="11" height="9" fill="#b81d25"/><path d="M0 0l5.5 5L11 0" stroke="#fff" fill="none"/></svg>info@bramblecourtelectric.com</div>
  <div class="contact-line"><svg width="10" height="13" viewBox="0 0 10 13"><path d="M5 0a5 5 0 015 5c0 3.5-5 8-5 8S0 8.5 0 5a5 5 0 015-5z" fill="#b81d25"/></svg>1420 Alder Row NE Fenwick,<br>MN 55099</div>
</div>
<div class="abs foot-col" style="left:613px">
  <h4>Quick links</h4>
  <ul><li>Home</li><li>Company</li><li>Services</li><li>Service Area</li><li>Gallery</li><li>FAQs</li><li>Contact Us</li></ul>
</div>
<div class="abs foot-col" style="left:756px">
  <h4>Our services</h4>
  <ul><li>Commerical Electrical Services</li><li>Residential Electrical Services</li><li>Industrial Electrical Services</li></ul>
</div>
<span class="foot-social" style="top:2969px"></span>
<span class="foot-social" style="top:3006px;background:var(--red)"></span>
<span class="foot-social" style="top:3043px"></span>
<div class="abs copyright">© 2022 <strong>Bramblecourt Electric.</strong> All Right Reserved</div>
<div class="abs legal"><span>Privacy Policy</span><span>|</span><span>Terms of Use</span><span>|</span><span>Cookie Policy</span></div>
<svg class="abs" style="left:968px;top:3164px" width="14" height="16" viewBox="0 0 14 16"><path d="M7 0l7 16-7-4-7 4z" fill="#bbbbbd"/></svg>

</body>
</html>
```